CD-/Plattencover für Tonträgerfirma
Zielgruppe
Wir sind eine Tonträgerfirma und bewegen uns im Low-Budget-Segment.
Aufgabenstellung
Für eine KLassik Serie benötigen wir 7 Cover, welche aber im Grundlayout immer gleich seinen sollten. Es soll eine erkenntliche Serie entstehen.
Das Thema lautet: Velvet Hour
Die Unterthemen lauten:
1. The Amber Lantern Gathering
2. The Velvet Hour Riverside Suites
3. The Velvet Hour Meadow Steps
4. The Velvet Hour Moonlit Whispers
5. The Copper Table Evenings
6. The Silver Curtain Soirée
7. The Northwind Orchestral Treasures
Wir benötigen nicht das komplette Artwork, sondern ein Frontcover
(12 x 12 cm + 2 cm Beschnitt wg. etwaiger Verschiebung der Positionierung
Fertigstellung (Aufziehen des Inlays und Labels) erfolgt später bei uns im Hause
Wir benötigen später offene psd-Dateien mit allen Ebenen
Wichtig: Schriften nicht gerastert ggfs. Schrift mitliefern

```html
<!DOCTYPE html>
<html lang="en">
<head>
<meta charset="utf-8">
<title>Velvet Hour – Cover Series</title>
<link rel="stylesheet" href="https://fonts.googleapis.com/css2?family=Cinzel:wght@600;700&family=Cabin:wght@700&display=swap">
<style>
  :root {
    --canvas: #ffffff;
    --cover-bg: #000000;
    --frame: #b3205c;
    --red: #b2221f;
    --orange: #b8682a;
    --yellow: #c9b73a;
    --green: #2f7d2c;
    --blue: #2a2fa8;
    --violet: #6a1f7a;
    --type-light: #fbf4ff;
    --type-mid: #e2c2f2;
    --type-deep: #a765cc;
    --flourish: rgba(170, 170, 185, 0.18);
  }
  * { box-sizing: border-box; margin: 0; padding: 0; }
  html, body {
    width: 1200px; height: 615px; overflow: hidden;
    background: var(--canvas);
  }
  .series { position: relative; width: 1200px; height: 615px; }
  .cover {
    position: absolute; width: 284px; height: 283px;
    background: var(--cover-bg);
    border: 1px solid var(--frame);
    overflow: hidden;
  }
  .cover-photo {
    position: absolute; inset: 0 0 22% 0;
    background: var(--photo);
  }
  .colour-bands {
    position: absolute; inset: 0 0 22% 0;
    background: linear-gradient(90deg,
      var(--red) 0 16.6%, var(--orange) 16.6% 33.3%, var(--yellow) 33.3% 50%,
      var(--green) 50% 66.6%, var(--blue) 66.6% 83.3%, var(--violet) 83.3% 100%);
    opacity: 0.5;
    mix-blend-mode: hard-light;
  }
  .fade {
    position: absolute; inset: 0;
    background: linear-gradient(180deg, rgba(0,0,0,0) 50%, rgba(0,0,0,0.85) 68%, var(--cover-bg) 78%);
  }
  .flourish {
    position: absolute; left: 14px; right: 14px; bottom: 4px; height: 56px;
    background: radial-gradient(ellipse at center, var(--flourish), transparent 70%);
  }
  .cover-title { position: absolute; inset: 0; }
  .cover-title span {
    position: absolute; left: 0; right: 0;
    text-align: center; line-height: 1; white-space: nowrap;
    background: linear-gradient(180deg, var(--type-light) 0%, var(--type-mid) 50%, var(--type-deep) 100%);
    -webkit-background-clip: text; background-clip: text; color: transparent;
    filter: drop-shadow(0 1px 1px rgba(0,0,0,0.9));
  }
  .title-lead {
    top: 176px;
    font-family: "Cabin", sans-serif; font-weight: 700;
    font-size: 27px; letter-spacing: 1px;
  }
  .title-lead.long { font-size: 22px; top: 179px; }
  .title-line {
    font-family: "Cinzel", serif; font-weight: 700;
    font-size: 30px;
  }
  .line-1 { top: 210px; }
  .line-2 { top: 243px; }
  .title-line.narrow { font-size: 25px; }

  .c1 { left: 20px;  top: 19px;
    --photo: radial-gradient(ellipse 38% 45% at 48% 38%, #f3d67a, #a67a24 55%, transparent 80%), linear-gradient(160deg, #4a1a10, #1a0c2a 80%); }
  .c2 { left: 312px; top: 19px;
    --photo: radial-gradient(ellipse 35% 50% at 42% 45%, #c7823c, #6b3416 60%, transparent 85%), linear-gradient(135deg, #3a0d0d, #140818); }
  .c3 { left: 603px; top: 19px;
    --photo: radial-gradient(ellipse 22% 40% at 52% 42%, #6b4a32, transparent 80%), linear-gradient(180deg, #d9b58a, #b5865a); }
  .c4 { left: 895px; top: 19px;
    --photo: radial-gradient(circle at 80% 22%, #f5f3ea 0 18%, #c9c4b4 24%, transparent 34%), radial-gradient(ellipse 10% 40% at 72% 55%, #0d0d1a, transparent), linear-gradient(180deg, #3a2a3c, #8c6a66 60%, #1c1414); }
  .c5 { left: 166px; top: 313px;
    --photo: linear-gradient(155deg, #6b2a12 0%, #c9803a 40%, #7a3a18 60%, #2a120c 100%); }
  .c6 { left: 457px; top: 313px;
    --photo: repeating-linear-gradient(180deg, #f1d77a 0 10px, #b3702c 10px 26px), #b3702c; }
  .c7 { left: 749px; top: 313px;
    --photo: radial-gradient(ellipse 30% 45% at 45% 40%, #c9a06a, transparent 75%), linear-gradient(135deg, #5a1410, #1c0a10 80%); }
</style>
</head>
<body>
<main class="series">

  <section class="cover c1">
    <div class="cover-photo" role="img" aria-label="Golden Venetian carnival mask with feathers"></div>
    <div class="colour-bands"></div>
    <div class="fade"></div>
    <div class="flourish" role="img" aria-label="Faint scrollwork ornament"></div>
    <h2 class="cover-title">
      <span class="title-lead">THE AMBER</span>
      <span class="title-line line-1">LANTERN</span>
      <span class="title-line line-2">GATHERING</span>
    </h2>
  </section>

  <section class="cover c2">
    <div class="cover-photo" role="img" aria-label="Cellist's hands bowing a cello"></div>
    <div class="colour-bands"></div>
    <div class="fade"></div>
    <div class="flourish" role="img" aria-label="Faint scrollwork ornament"></div>
    <h2 class="cover-title">
      <span class="title-lead long">THE VELVET HOUR</span>
      <span class="title-line line-1">RIVERSIDE</span>
      <span class="title-line line-2">SUITES</span>
    </h2>
  </section>

  <section class="cover c3">
    <div class="cover-photo" role="img" aria-label="Male ballet dancer leaping mid-air"></div>
    <div class="colour-bands"></div>
    <div class="fade"></div>
    <div class="flourish" role="img" aria-label="Faint scrollwork ornament"></div>
    <h2 class="cover-title">
      <span class="title-lead long">THE VELVET HOUR</span>
      <span class="title-line line-1">MEADOW</span>
      <span class="title-line line-2">STEPS</span>
    </h2>
  </section>

  <section class="cover c4">
    <div class="cover-photo" role="img" aria-label="Violinist silhouetted before a full moon in a starry sky"></div>
    <div class="colour-bands"></div>
    <div class="fade"></div>
    <div class="flourish" role="img" aria-label="Faint scrollwork ornament"></div>
    <h2 class="cover-title">
      <span class="title-lead long">THE VELVET HOUR</span>
      <span class="title-line line-1">MOONLIT</span>
      <span class="title-line line-2">WHISPERS</span>
    </h2>
  </section>

  <section class="cover c5">
    <div class="cover-photo" role="img" aria-label="Violin and glass of wine on a wooden table"></div>
    <div class="colour-bands"></div>
    <div class="fade"></div>
    <div class="flourish" role="img" aria-label="Faint scrollwork ornament"></div>
    <h2 class="cover-title">
      <span class="title-lead">THE COPPER</span>
      <span class="title-line line-1">TABLE</span>
      <span class="title-line line-2">EVENINGS</span>
    </h2>
  </section>

  <section class="cover c6">
    <div class="cover-photo" role="img" aria-label="Ornate lit opera house balconies"></div>
    <div class="colour-bands"></div>
    <div class="fade"></div>
    <div class="flourish" role="img" aria-label="Faint scrollwork ornament"></div>
    <h2 class="cover-title">
      <span class="title-lead">THE SILVER</span>
      <span class="title-line line-1">CURTAIN</span>
      <span class="title-line line-2">SOIRÉE</span>
    </h2>
  </section>

  <section class="cover c7">
    <div class="cover-photo" role="img" aria-label="Orchestra violinists performing on stage"></div>
    <div class="colour-bands"></div>
    <div class="fade"></div>
    <div class="flourish" role="img" aria-label="Faint scrollwork ornament"></div>
    <h2 class="cover-title">
      <span class="title-lead">THE NORTHWIND</span>
      <span class="title-line line-1 narrow">ORCHESTRAL</span>
      <span class="title-line line-2 narrow">TREASURES</span>
    </h2>
  </section>

</main>
</body>
</html>
```